Adult Literacy Program - flyer to attract volunteers and students

We want a flyer that is engaging, colorful, modern and will appeal to our primary audience of adults aged 40-60. We are trying to attract both prospective volunteers (typically age 50+, mostly women) and students (typically aged 40+).
The flyer should feature diverse people working together in pairs of two, reading or talking, with a workbook or some reading material in front of them.

Our organization trains tutors to work one-on-one with adults who are learning how to read. Most of our adult students are non-native speakers of English. Many are of Haitian or Hispanic origin, so we would like some people who represent that demographic.

The Flyer should represent reading, learning, literacy, knowledge, growth,
and opportunities.
Our students are learning to read so they can advance their job opportunities.

Target Market(s)

Adults aged 40-60, primarily women, retired, volunteers

Industry/Entity Type

Education

Font styles to use
Serif
Sans Serif

Colors

Designer to choose colors to be used in the design.

Requirements
Must have
• - UPDATE: Should be designed as a TRI-FOLD brochure on 8.5 x 11 inch paper that will be folded into thirds.
• - Images of diverse people, women and men, who look Hispanic, Haitian and other nationalities as well as Caucasian.
• - Our logo on the front cover
Nice to have
• The sample flyer is very boring and dry! We are open to different ways of presenting the text.

```html
<!DOCTYPE html>
<html lang="en">
<head>
<meta charset="utf-8">
<title>Adult Literacy Program – Tri-fold Brochure</title>
<link rel="stylesheet" href="https://fonts.googleapis.com/css2?family=Didact+Gothic&family=Oswald:wght@600&family=Open+Sans:ital,wght@0,600;0,700;1,700&family=Parisienne&display=swap">
<style>
  :root {
    --page-bg: #d9d9d9;
    --paper: #ffffff;
    --paper-mid: #f3f4f6;
    --brand-blue: #1ba3d8;
    --ring-blue: #7ccbea;
    --navy: #2a3668;
    --ink: #2b2b2b;
    --photo-warm: #c7a58a;
    --photo-shelf: #8a6a55;
  }
  * { box-sizing: border-box; margin: 0; padding: 0; }
  html, body { width: 1200px; height: 899px; overflow: hidden; }
  body { background: var(--page-bg); font-family: "Didact Gothic", Arial, sans-serif; color: var(--ink); }

  .brochure {
    position: absolute; left: 72px; top: 41px;
    width: 1056px; height: 816px;
    display: flex;
    box-shadow: 0 6px 24px rgba(0,0,0,.18);
  }
  .panel { position: relative; width: 352px; height: 816px; overflow: hidden; background: var(--paper); }
  .panel--center { background: var(--paper-mid); }

  .section-head { position: absolute; top: 70px; left: 34px; display: flex; align-items: center; gap: 8px; }
  .section-head__icon { width: 46px; height: 46px; }
  .section-head__tab {
    background: var(--brand-blue); color: #fff;
    font-family: "Oswald", Arial, sans-serif; font-weight: 600; font-size: 22px; letter-spacing: .5px;
    padding: 4px 40px 4px 46px;
    clip-path: polygon(0 0, 94% 0, 100% 100%, 0 100%);
    border-radius: 4px 0 0 4px;
  }

  .bullets { position: absolute; top: 142px; left: 40px; right: 26px; list-style: none; }
  .bullets li { position: relative; padding-left: 18px; font-size: 17px; line-height: 1.15; margin-bottom: 10px; }
  .bullets li::before { content: ""; position: absolute; left: 0; top: 8px; width: 6px; height: 6px; border-radius: 50%; background: var(--brand-blue); }
  .bullets .sub { display: block; padding-left: 6px; }

  .script-quote { position: absolute; left: 40px; right: 24px; font-family: "Parisienne", cursive; font-size: 32px; line-height: 1.15; color: #222; }

  .photo-disc {
    position: absolute; border-radius: 50%;
    border: 6px solid var(--ring-blue);
    background: radial-gradient(circle at 45% 40%, var(--photo-warm), var(--photo-shelf));
  }
  .photo-disc--tutors { width: 520px; height: 520px; left: -30px; top: 600px; }
  .photo-disc--center { width: 300px; height: 300px; left: 26px; top: -60px; }
  .photo-disc--students { width: 460px; height: 460px; left: 24px; top: 520px;
    background: radial-gradient(circle at 40% 40%, #a9c4dc, #6f5e52); }

  .book-mark { position: absolute; left: 116px; top: 282px; width: 120px; height: 100px; }

  .cta { position: absolute; top: 410px; left: 0; right: 0; text-align: center; }
  .cta__head { font-family: "Open Sans", Arial, sans-serif; font-weight: 700; font-size: 21px; color: var(--navy); }
  .cta__sub { font-family: "Open Sans", Arial, sans-serif; font-weight: 700; font-style: italic; font-size: 17px; color: var(--brand-blue); margin-bottom: 18px; }
  .cta__line { font-size: 17px; line-height: 1.45; }
  .cta__line strong { font-family: "Open Sans", Arial, sans-serif; font-weight: 600; }

  .org-name { position: absolute; top: 640px; left: 0; right: 0; display: flex; justify-content: center; align-items: center; gap: 8px; }
  .org-name__dot { width: 18px; height: 18px; border-radius: 50%; background: var(--brand-blue); }
  .org-name__text { font-family: "Open Sans", Arial, sans-serif; font-weight: 700; font-size: 17px; color: var(--navy); }
</style>
</head>
<body>
  <main class="brochure">
    <section class="panel panel--tutors">
      <header class="section-head">
        <svg class="section-head__icon" viewBox="0 0 46 46" aria-hidden="true">
          <circle cx="26" cy="12" r="8" fill="#1ba3d8"/>
          <path d="M12 40 C12 26 40 26 40 40 Z" fill="#1ba3d8"/>
          <polygon points="10,22 13,30 21,30 15,35 17,43 10,38 3,43 5,35 -1,30 7,30" fill="#1ba3d8" stroke="#fff" stroke-width="1.5"/>
        </svg>
        <h2 class="section-head__tab">TUTORS</h2>
      </header>
      <ul class="bullets">
        <li>No special skills or degrees needed - just a degree of caring!</li>
        <li>Training offered throughout the year</li>
        <li>Tutors meet students weekly at a library</li>
        <li>Instructional materials provided</li>
        <li>Ongoing support available</li>
      </ul>
      <p class="script-quote" style="top:420px">Teach an adult to read and you'll change a life forever.</p>
      <div class="photo-disc photo-disc--tutors" role="img" aria-label="Photo of a volunteer tutor and an adult student reading a book together in a library"></div>
    </section>

    <section class="panel panel--center">
      <div class="photo-disc photo-disc--center" role="img" aria-label="Photo of a smiling woman at a library table with other adult learners"></div>
      <div class="book-mark" role="img" aria-label="Illustration of an open book with pages lifting like birds" style="background:linear-gradient(180deg,#7ccbea 0%,#1ba3d8 55%,#2a3668 100%);border-radius:6px 6px 40% 40%;"></div>
      <div class="cta">
        <p class="cta__head">DON'T WASTE A MOMENT!</p>
        <p class="cta__sub">Contact Us Today to Learn More!</p>
        <p class="cta__line">Volunteer Desk: <strong>555-214-7380</strong></p>
        <p class="cta__line">Millbrook, Oakvale</p>
        <p class="cta__line">&amp; Cedar Point: <strong>555-318-6042</strong></p>
        <p class="cta__line">email: <strong>literacy@riverbendlibrary.org</strong></p>
      </div>
      <div class="org-name">
        <span class="org-name__dot"></span>
        <span class="org-name__text">Riverbend Library</span>
      </div>
    </section>

    <section class="panel panel--students">
      <header class="section-head">
        <svg class="section-head__icon" viewBox="0 0 46 46" aria-hidden="true">
          <circle cx="23" cy="11" r="8" fill="#1ba3d8"/>
          <path d="M7 42 C7 24 39 24 39 42 Z" fill="#1ba3d8"/>
          <path d="M11 30 L23 34 L35 30 L35 42 L23 45 L11 42 Z" fill="#fff" stroke="#1ba3d8" stroke-width="2"/>
          <line x1="23" y1="34" x2="23" y2="45" stroke="#1ba3d8" stroke-width="2"/>
        </svg>
        <h2 class="section-head__tab">STUDENTS</h2>
      </header>
      <ul class="bullets">
        <li>Students are adults in need of:
          <span class="sub">· basic literacy skills</span>
          <span class="sub">· pre-GED skills</span>
          <span class="sub">· conversational English</span></li>
        <li>Tutoring is free of charge</li>
        <li>Tutoring is one-on-one</li>
        <li>Flexible scheduling during library hours</li>
        <li>Lessons focus on student goals</li>
      </ul>
      <p class="script-quote" style="top:442px">If you can read, you can tutor!</p>
      <div class="photo-disc photo-disc--students" role="img" aria-label="Photo of an older man and a tutor working through a workbook together"></div>
    </section>
  </main>
</body>
</html>
```